Letterhead and Envelope Only (no biz card)
Leadership Development & Coaching Start Up
I also really like it when the swirls are not perfectly positioned on the page...bleeding off the page looks good. Thanks everyone!
Thanks for submitting your designs! Something else to keep in mind, I am rather feminine...I prefer softer lines and fainter watermarks in the background. I also really prefer the contact info to be on the bottom of the design.
Correction, I like the contact info on the bottom in #1 (not #3.)
My logo designer is out of the country, I should have those files for you in the next couple of days.
From the three designs so far, I like the swirls in #2. I like the contact info on the bottom in #3.
If possible, I'd like to have 2 letterhead designs in my winner...so I can use both for various purposes.
could you please upload the ai or eps file of logo?

```html
<!DOCTYPE html>
<html lang="en">
<head>
<meta charset="utf-8">
<title>Velmora Stationery — Letterhead &amp; Envelope</title>
<link href="https://fonts.googleapis.com/css2?family=Arimo:wght@400;700&display=swap" rel="stylesheet">
<style>
  :root {
    --navy: #1f3f8a;
    --gold: #f9b316;
    --paper: #ffffff;
    --backdrop: #ffffff;
    --ink: #2a3550;
    --swirl-tint: #faf3da;
    --edge: #d9d9d9;
  }
  * { margin: 0; padding: 0; box-sizing: border-box; }
  html, body {
    width: 1200px; height: 1101px; overflow: hidden;
    background: var(--backdrop);
    font-family: "Arimo", Arial, sans-serif;
  }
  .stage { position: relative; width: 1200px; height: 1101px; }

  /* Letterhead */
  .letterhead {
    position: absolute; left: 36px; top: 24px; width: 795px; height: 1044px;
    background: var(--paper); border: 1px solid var(--edge);
    box-shadow: 2px 3px 8px rgba(0,0,0,.12); overflow: hidden;
  }
  .letterhead__watermark {
    position: absolute; left: -40px; top: 170px; width: 500px; height: 720px;
    background: radial-gradient(ellipse at 45% 45%, var(--swirl-tint) 0%, rgba(250,243,218,.5) 45%, rgba(255,255,255,0) 72%);
  }
  .brand {
    position: absolute; display: flex; align-items: center; gap: 10px;
    color: var(--navy); font-weight: 700; letter-spacing: -0.5px; line-height: 1;
  }
  .brand__dot { border-radius: 50%; background: var(--gold); flex: none; }
  .letterhead .brand { left: 228px; top: 78px; font-size: 46px; }
  .letterhead .brand__dot { width: 28px; height: 28px; }
  .letterhead__contact {
    position: absolute; left: 0; width: 795px; top: 962px;
    text-align: center; font-size: 12.5px; line-height: 1.55; color: var(--ink);
    font-style: normal;
  }
  .corner-arc { position: absolute; right: 0; bottom: 0; display: block; }

  /* Envelope */
  .envelope {
    position: absolute; left: 369px; top: 390px; width: 822px; height: 504px;
    filter: drop-shadow(2px 3px 6px rgba(0,0,0,.15));
  }
  .envelope svg.envelope__shape { position: absolute; inset: 0; }
  .envelope .brand { left: 501px; top: 210px; font-size: 38px; }
  .envelope .brand__dot { width: 22px; height: 22px; }
  .envelope__address {
    position: absolute; left: 510px; top: 293px; font-size: 12.5px; color: var(--ink);
  }
</style>
</head>
<body>
<main class="stage">

  <section class="letterhead" aria-label="Letterhead">
    <div class="letterhead__watermark" role="img" aria-label="Faint swirl watermark bleeding off the left edge"></div>
    <div class="brand"><span>velmora</span><span class="brand__dot"></span></div>
    <address class="letterhead__contact">
      4820 Larkspur Lane Fenwick, CO 80219<br>
      P: 303.555.0148&nbsp;&nbsp;E: jmarlow@themarlowgroup.com<br>
      www.velmoragroup.com
    </address>
    <svg class="corner-arc" width="216" height="114" viewBox="0 0 216 114" aria-hidden="true">
      <path d="M0 114 C30 45 120 2 216 0 L216 114 Z" fill="var(--gold)"/>
    </svg>
  </section>

  <section class="envelope" aria-label="Envelope">
    <svg class="envelope__shape" width="822" height="504" viewBox="0 0 822 504" aria-hidden="true">
      <rect x="0.5" y="114" width="821" height="389.5" fill="var(--paper)" stroke="var(--edge)"/>
      <path d="M0 144 L0 114 C150 40 300 0 405 0 C520 0 680 40 822 105 L822 144 Z" fill="var(--navy)"/>
      <circle cx="405" cy="72" r="11" fill="var(--gold)"/>
      <path d="M585 504 C620 430 720 384 822 384 L822 504 Z" fill="var(--gold)"/>
    </svg>
    <div class="brand"><span>velmora</span><span class="brand__dot"></span></div>
    <p class="envelope__address">4820 Larkspur Lane Fenwick, CO 80219</p>
  </section>

</main>
</body>
</html>
```